Business Card for my New Brokerage

Looking to get a business card design for my new Real Estate Brokerage.
I want it with Picture, Phone Number, Email, Website, Office Address
Name and Designation. Please add logo too.

Target Market(s)

Real Estate Investors or Home Buyers

Industry/Entity Type

Real Estate

Contact Information for Business Card

Name, Email, Phone Number, website, email, office address

Colors
EB3D1F
EC4F4E
F09395
F8D3D4
FCEDEE

Requirements
Must have
• Minimalistic, Clean, Modern, Photo
Nice to have
• White and Red Colors

```html
<!DOCTYPE html>
<html lang="en">
<head>
<meta charset="utf-8">
<title>Ember Realty Inc – Business Card</title>
<link href="https://fonts.googleapis.com/css2?family=Montserrat:wght@400;500;600&display=swap" rel="stylesheet">
<style>
  :root{
    --brand-red:#dd0000;
    --brand-red-deep:#b30000;
    --gold:#dcb862;
    --ink:#4a4a4a;
    --paper:#ffffff;
    --backdrop:#1d1d1d;
    --photo-light:#eef1f5;
    --photo-dark:#1f2638;
  }
  html,body{margin:0;padding:0;width:1200px;height:1199px;overflow:hidden;background:var(--backdrop);}
  body{position:relative;font-family:"Montserrat",Arial,sans-serif;}
  .card{position:absolute;left:195px;width:800px;height:435px;overflow:hidden;}
  .card--front{top:115px;background:var(--paper);}
  .card--back{top:649px;background:var(--brand-red);display:flex;align-items:center;justify-content:center;}
  .portrait{position:absolute;left:0;top:0;width:310px;height:335px;
    background:linear-gradient(180deg,var(--photo-light) 0%,#c9d3e0 55%,var(--photo-dark) 100%);}
  .bands{position:absolute;left:0;top:0;width:800px;height:435px;}
  .holder{position:absolute;left:36px;top:343px;color:var(--paper);}
  .holder__name{margin:0;font-size:29px;font-weight:600;letter-spacing:1px;line-height:1.1;}
  .holder__title{margin:6px 0 0;font-size:18px;font-weight:400;letter-spacing:.5px;}
  .brand{position:absolute;right:50px;top:92px;display:flex;align-items:center;gap:10px;}
  .brand__name{font-size:30px;font-weight:600;color:var(--brand-red);letter-spacing:2px;white-space:nowrap;}
  .brand__mark{width:12px;height:12px;background:var(--gold);}
  .contact{position:absolute;right:49px;top:206px;text-align:right;color:var(--ink);font-size:18.5px;letter-spacing:.3px;}
  .contact__address{margin:0;line-height:26px;}
  .contact__rule{width:21px;height:2px;background:var(--brand-red);margin:10px 0 12px auto;}
  .contact__line{display:flex;justify-content:flex-end;align-items:center;gap:8px;height:26.5px;}
  .contact__icon{width:12px;height:12px;flex:none;}
  .back-brand{display:flex;align-items:center;gap:14px;}
  .back-brand__name{font-size:46px;font-weight:600;color:#c8c8c8;letter-spacing:3px;white-space:nowrap;}
  .back-brand__mark{width:16px;height:16px;background:var(--brand-red-deep);}
</style>
</head>
<body>
  <section class="card card--front">
    <div class="portrait" role="img" aria-label="Portrait photo of the broker in a navy blazer and light blue shirt"></div>
    <svg class="bands" viewBox="0 0 800 435" aria-hidden="true">
      <polygon points="0,335 312,335 386,407 800,407 800,435 0,435" fill="var(--brand-red)"/>
      <polygon points="380,385 800,385 800,400 394,400" fill="var(--gold)"/>
    </svg>
    <div class="holder">
      <p class="holder__name">DANIEL REYES</p>
      <p class="holder__title">Founder and President</p>
    </div>
    <div class="brand">
      <span class="brand__mark"></span>
      <span class="brand__name">EMBER REALTY INC</span>
    </div>
    <div class="contact">
      <p class="contact__address">1870 Harbor Mill Road<br>Riverton, GA 30412</p>
      <div class="contact__rule"></div>
      <div class="contact__line">+330 5180-4725
        <svg class="contact__icon" viewBox="0 0 12 12"><path d="M3 1 L5 3.5 L4 5 Q5.5 7.5 7 8 L8.5 7 L11 9 L9.5 11 Q4 10 1 2.5 Z" fill="var(--brand-red)"/></svg>
      </div>
      <div class="contact__line">hello@emberrealtyinc.com
        <svg class="contact__icon" viewBox="0 0 12 12"><rect x="1" y="2.5" width="10" height="7" fill="none" stroke="var(--brand-red)" stroke-width="1.3"/><path d="M1 3 L6 6.5 L11 3" fill="none" stroke="var(--brand-red)" stroke-width="1.3"/></svg>
      </div>
      <div class="contact__line">www.emberrealtyinc.com
        <svg class="contact__icon" viewBox="0 0 12 12"><circle cx="6" cy="6" r="5" fill="none" stroke="var(--brand-red)" stroke-width="1.2"/><ellipse cx="6" cy="6" rx="2.2" ry="5" fill="none" stroke="var(--brand-red)" stroke-width="1"/><path d="M1 6 H11 M2 3.5 H10 M2 8.5 H10" stroke="var(--brand-red)" stroke-width="1"/></svg>
      </div>
    </div>
  </section>

  <section class="card card--back">
    <div class="back-brand">
      <span class="back-brand__mark"></span>
      <span class="back-brand__name">EMBER REALTY INC</span>
    </div>
  </section>
</body>
</html>
```